Cover design needed for scholarship book whose intended audience is students with medical conditions

I need a book cover designed for a book called, “The Thistle Grant: How To Make Your Health Challenge Pay Your Way Through School.” This book is aimed at students with a variety of medical conditions. I wrote The Thistle Grant after I received a medical-based scholarship ($96,000) to attend college and law school based on my allergies to pollen—hence the title. However, this government program applies to just about any medical condition—not just allergies. I have assisted students in applying for this program who suffer from many different medical conditions. So I would like the cover design to convey that message—that this program applies to many different medical conditions. One of the big misconceptions about medical-based scholarships is you will only qualify if you have a really serious medical condition. So I would like to see some cover designs that list some common medical conditions in order to convey to the reader that many different medical conditions qualify. A few possible medical conditions are allergies, asthma, ADHD, depression, anxiety, back pain, eating disorders, bipolar, sleep disorders, and OCD. Possible ways to convey this may be to have the names of some of these common medical conditions written on graduation caps or randomly dispersed in the background, etc. However, this isn’t the only theme I would like to see. In essence, I give you creative liberty to wow me with your design prowess. The point of crowd design is to get variety of designs to choose from that I may not have thought of on my own. I have dabbled with some ideas that blend the themes of the education world and the medical world and I think this is the essence of the book. What ever you come up with, it needs to make it clear at a glance that this book helps you pay for college on the basis of your medical condition—whatever medical condition that may be. To see a simple mock up I did (that I don't want to use) go to healthtuitionaid.example

The book is 153 pages on 5x8 paper. I am planning to print the book through PrintHarbor, so the cover should adhere to the PrintHarbor design requirements. I can provide the PrintHarbor template if needed.

Updates: Please be able to provide a few updates to the cover design if your design is selected. After choosing the final design, physical proofs of the book will be ordered so I can see what your design looks like in real life. After the proofs are reviewed, I may need some minor changes (i.e., maybe the back cover text needs a new font size, etc..) Also, after I use the proofs to solicit endorsements, I am planning to purchase my own ISBN number and barcode. I would like the designer to be able to update my cover to include a new ISBN and barcode after the initial proofs are printed which should be 3-4 weeks later. So please be able to provide a few updates to the cover design if your design is selected.

Target Market(s)

Students/parents who are planning to attend college and have some type of medical condition

Industry/Entity Type

College

Font styles to use
Serif

Requirements
Must have
• My project must have a general education/medical theme
Nice to have
• I'd like to see some designs that include random medical conditions dispersed on the cover. Maybe a different medical condition written on several different graduation caps, or some other context.
Should not have
• The cover design should not depict persons with severe medical conditions--i.e., people in wheelchairs, hospital beds, etc.

```html
<!DOCTYPE html>
<html lang="en">
<head>
<meta charset="utf-8">
<title>The Thistle Grant – Cover Options</title>
<link rel="stylesheet" href="https://fonts.googleapis.com/css2?family=Libre+Baskerville:ital,wght@0,400;0,700;1,400&family=Montserrat:wght@700&family=Didact+Gothic&family=Open+Sans:wght@800&display=swap">
<style>
  :root {
    --backdrop: #b8733c;
    --sky: #29a6e0;
    --sky-mid: #7cc3ec;
    --sky-light: #bfe3f6;
    --sky-pale: #eaf6fd;
    --slate: #68686b;
    --slate-line: #8c8c8f;
    --ink: #3a3a3c;
    --cap: #262628;
    --paper: #ffffff;
    --mist: #ececee;
  }
  * { box-sizing: border-box; margin: 0; padding: 0; }
  html, body { width: 1200px; height: 1200px; overflow: hidden; }
  body { background: var(--backdrop); position: relative; }

  .cover {
    position: absolute; top: 172px; width: 536px; height: 856px;
    overflow: hidden; box-shadow: 0 6px 18px rgba(0,0,0,.25);
  }
  .cover-art { position: absolute; left: 0; }
  .option-label {
    position: absolute; top: 1068px; width: 536px; text-align: center;
    font-family: "Open Sans", sans-serif; font-weight: 800; font-size: 38px;
    color: var(--paper); letter-spacing: -.5px;
  }

  /* Option 1 – classic serif */
  .cover--classic { left: 40px; background: var(--paper); }
  .classic-title {
    position: absolute; top: 26px; width: 100%; text-align: center;
    font-family: "Libre Baskerville", serif; font-weight: 400; font-size: 60px; color: var(--sky);
    line-height: 1; letter-spacing: -1px;
  }
  .classic-band {
    position: absolute; top: 92px; left: 92px; width: 352px; height: 52px;
    background: var(--sky); color: var(--paper); text-align: center;
    font-family: "Libre Baskerville", serif; font-weight: 700; font-size: 36px;
    line-height: 54px; letter-spacing: 1px;
  }
  .classic-rule { position: absolute; top: 145px; left: 0; width: 100%; height: 8px; background: var(--slate-line); }
  .classic-art { top: 153px; }
  .circle-label { font-family: "Libre Baskerville", serif; font-weight: 700; fill: var(--sky); text-anchor: middle; }
  .classic-stripe { position: absolute; left: 0; width: 100%; height: 10px; background: var(--sky); }
  .classic-subtitle {
    position: absolute; top: 708px; left: 0; width: 100%; height: 84px;
    background: var(--slate); color: var(--paper); text-align: center;
    font-family: "Libre Baskerville", serif; font-size: 23px; line-height: 32px; padding-top: 10px;
  }
  .classic-subtitle .accent { color: var(--sky); font-weight: 700; }
  .classic-author {
    position: absolute; top: 816px; width: 100%; text-align: center;
    font-family: "Libre Baskerville", serif; font-style: italic; font-size: 22px; color: var(--ink);
  }

  /* Option 2 – modern sans */
  .cover--modern {
    left: 624px;
    background: linear-gradient(180deg, var(--paper) 0%, var(--sky-pale) 30%, #bfe3f7 70%, #8fcdf0 100%);
  }
  .modern-title {
    position: absolute; top: 58px; right: 32px; text-align: right;
    font-family: "Montserrat", sans-serif; font-weight: 700; line-height: 1;
  }
  .modern-title .main { display: block; font-size: 64px; color: var(--sky); letter-spacing: 1px; }
  .modern-title .sub { display: block; font-size: 54px; color: var(--ink); margin-top: 2px; }
  .modern-art { top: 0; }
  .condition-tag { font-family: "Montserrat", sans-serif; font-weight: 700; font-size: 10px; letter-spacing: .6px; fill: var(--paper); text-anchor: middle; }
  .modern-band {
    position: absolute; top: 698px; left: 0; width: 100%; height: 90px;
    background: var(--sky); color: var(--paper);
    font-family: "Didact Gothic", sans-serif; font-size: 26px; line-height: 34px;
    padding: 12px 0 0 30px;
  }
  .modern-band .highlight { background: var(--paper); color: var(--sky); padding: 0 5px; font-family: "Montserrat", sans-serif; font-weight: 700; font-size: 23px; }
  .modern-author {
    position: absolute; top: 790px; left: 30px; background: var(--slate-line); color: var(--paper);
    font-family: "Didact Gothic", sans-serif; font-size: 18px; padding: 1px 6px;
  }
</style>
</head>
<body>

  <section class="cover cover--classic">
    <h1 class="classic-title">The Thistle</h1>
    <div class="classic-band">GRANT</div>
    <div class="classic-rule"></div>

    <svg class="cover-art classic-art" width="536" height="545" viewBox="0 0 536 545">
      <defs>
        <linearGradient id="mistFade" x1="0" x2="1">
          <stop offset="0" stop-color="#f3f3f5"/><stop offset="1" stop-color="#e4e4e7"/>
        </linearGradient>
        <linearGradient id="skyColumn" x1="0" x2="1">
          <stop offset="0" stop-color="#5fb3e6"/><stop offset="1" stop-color="#a9d8f4"/>
        </linearGradient>
      </defs>
      <rect width="536" height="545" fill="url(#mistFade)"/>
      <path d="M170 0 H520 C470 140 430 240 420 300 C410 380 460 470 500 545 H180 C230 460 260 380 240 300 C220 220 190 120 170 0 Z" fill="url(#skyColumn)"/>

      <g class="condition-circle">
        <circle cx="128" cy="87" r="76" fill="#f7f7f8" stroke="#fff" stroke-width="10"/>
        <text class="circle-label" x="128" y="93" font-size="16">Allergies</text>
      </g>
      <g class="condition-circle">
        <circle cx="456" cy="67" r="52" fill="#f4f4f6" stroke="#fff" stroke-width="8"/>
        <text class="circle-label" x="456" y="73" font-size="16">OCD</text>
      </g>
      <g class="condition-circle">
        <circle cx="354" cy="141" r="100" fill="var(--sky-mid)" stroke="#fff" stroke-width="12"/>
        <path d="M347 88 h14 v14 h14 v14 h-14 v14 h-14 v-14 h-14 v-14 h14 z" fill="#fff"/>
        <text class="circle-label" x="354" y="168" font-size="19" fill="#fff" style="fill:#fff">Sleep</text>
        <text class="circle-label" x="354" y="192" font-size="19" style="fill:#fff">Disorders</text>
      </g>
      <g class="condition-circle">
        <circle cx="116" cy="227" r="36" fill="#f7f7f8" stroke="#fff" stroke-width="7"/>
        <text class="circle-label" x="116" y="232" font-size="13">ADHD</text>
      </g>
      <g class="condition-circle">
        <circle cx="240" cy="223" r="68" fill="#f4f4f6" stroke="#fff" stroke-width="10"/>
        <text class="circle-label" x="240" y="229" font-size="16">Asthma</text>
      </g>
      <g class="condition-circle">
        <circle cx="456" cy="231" r="60" fill="#f7f7f8" stroke="#fff" stroke-width="9"/>
        <text class="circle-label" x="456" y="237" font-size="15">Anxiety</text>
      </g>
      <g class="condition-circle">
        <circle cx="160" cy="391" r="64" fill="#f7f7f8" stroke="#fff" stroke-width="10"/>
        <text class="circle-label" x="160" y="397" font-size="14">Depression</text>
      </g>
      <g role="img" aria-label="Illustration: graduate wearing a mortarboard and a doctor's coat with stethoscope">
        <circle cx="348" cy="431" r="140" fill="var(--sky-light)" stroke="#fff" stroke-width="14"/>
      </g>
    </svg>

    <div class="classic-stripe" style="top:698px"></div>
    <p class="classic-subtitle">How To Make Your Health Challenge<br><span class="accent">Pay Your Way Through School</span></p>
    <div class="classic-stripe" style="top:792px"></div>
    <p class="classic-author">Dana Whitfield</p>
  </section>
  <div class="option-label" style="left:40px">OPTION1</div>

  <section class="cover cover--modern">
    <svg class="cover-art modern-art" width="536" height="698" viewBox="0 0 536 698">
      <g class="condition-tags">
        <g transform="translate(180 224) rotate(-35)"><rect x="-66" y="-11" width="132" height="22" rx="5" fill="var(--cap)"/><text class="condition-tag" y="4">EATING DISORDERS</text></g>
        <g transform="translate(84 296) rotate(-35)"><rect x="-42" y="-11" width="84" height="22" rx="5" fill="var(--cap)"/><text class="condition-tag" y="4">BACK PAIN</text></g>
        <g transform="translate(296 276) rotate(20)"><rect x="-36" y="-11" width="72" height="22" rx="5" fill="var(--cap)"/><text class="condition-tag" y="4">ASTHMA</text></g>
        <g transform="translate(194 358)"><rect x="-50" y="-11" width="100" height="22" rx="5" fill="var(--cap)"/><text class="condition-tag" y="4">DEPRESSION</text></g>
        <g transform="translate(428 380) rotate(-10)"><rect x="-64" y="-11" width="128" height="22" rx="5" fill="#4a4a4d"/><text class="condition-tag" y="4">SLEEP DISORDERS</text></g>
        <g transform="translate(70 476) rotate(40)"><rect x="-38" y="-11" width="76" height="22" rx="5" fill="#4a4a4d"/><text class="condition-tag" y="4">ANXIETY</text></g>
        <g transform="translate(240 456) rotate(-45)"><rect x="-44" y="-11" width="88" height="22" rx="5" fill="var(--cap)"/><text class="condition-tag" y="4">ALLERGIES</text></g>
        <g transform="translate(368 468) rotate(30)"><rect x="-24" y="-11" width="48" height="22" rx="5" fill="var(--cap)"/><text class="condition-tag" y="4">OCD</text></g>
        <g transform="translate(324 624) rotate(10)"><rect x="-28" y="-11" width="56" height="22" rx="5" fill="var(--cap)"/><text class="condition-tag" y="4">ADHD</text></g>
        <g transform="translate(456 584) rotate(-30)"><rect x="-36" y="-11" width="72" height="22" rx="5" fill="var(--cap)"/><text class="condition-tag" y="4">BIPOLAR</text></g>
      </g>
      <g role="img" aria-label="Illustration: smiling doctor in a white coat beneath tossed graduation caps and rolled diplomas">
        <rect x="40" y="508" width="188" height="190" rx="80" fill="#dcedf8"/>
      </g>
    </svg>
    <h1 class="modern-title"><span class="main">THE THISTLE</span><span class="sub">Grant</span></h1>
    <p class="modern-band">How To Make Your <span class="highlight">Health Challenge</span><br>Pay Your Way Through School</p>
    <p class="modern-author">Dana Whitfield</p>
  </section>
  <div class="option-label" style="left:624px">OPTION2</div>

</body>
</html>
```